Catering company looking to promote business

We need a flyer design for our company named "Peel and Pulp." We cater/deliver açaí bowls and smoothies.

The objective of this flyer is to let companies know that we are taking açaí bowls and smoothie orders and they can be delivered to them.

Some key points we would like on the flyer:
- Photo of açaí bowl and smoothie
- Menu w/ pricing
- "No hidden delivery fees"
- 5 bowl or smoothie minimum
- Online ordering through website:
https://tillbox.example/shop/peelandpulp
- For the month of February --> Get one free topping and drizzle!
- FRIDAY DELIVERIES ONLY
- Questions? Call (555) 730-9182
- social media friendwall & snapreel @pnpulp
- website www.peelandpulp.example

font - hello beautiful

Target Market(s)

Juice, smoothies, açaí bowls

Industry/Entity Type

Business

Font styles to use
Other font styles liked:
• Hello Beautiful

Colors
a64599
b768aa
d3a5cc
eedced
f7f1f7
9bcb3c

Requirements
Must have
• Please match logo, fonts, color schemes, etc.

```html
<!DOCTYPE html>
<html lang="en">
<head>
<meta charset="utf-8">
<title>Peel and Pulp – Açaí Bowl Flyer</title>
<link href="https://fonts.googleapis.com/css2?family=Montserrat:wght@500;600;700&family=Questrial&family=Kalam:wght@400;700&display=swap" rel="stylesheet">
<style>
  :root {
    --purple-deep: #7b3f98;
    --purple: #a64599;
    --purple-mid: #b768aa;
    --purple-soft: #d3a5cc;
    --purple-pale: #eedced;
    --purple-mist: #f7f1f7;
    --green: #9bcb3c;
    --green-dark: #6aa534;
    --red: #e2364f;
    --ink: #5a2f7a;
    --bar-dark: #6b3a8c;
    --bar-light: #b57cc4;
    --page: #ebe7ea;
    --white: #ffffff;
  }
  * { margin: 0; padding: 0; box-sizing: border-box; }
  html, body { width: 1200px; height: 3082px; overflow: hidden; }
  body { background: var(--page); position: relative; font-family: "Questrial", sans-serif; }

  .flyer {
    position: absolute; left: 50px; top: 746px;
    width: 1100px; height: 1590px;
    background: var(--white);
    box-shadow: 0 6px 24px rgba(60,30,70,.18);
    overflow: hidden;
  }

  .hero-photo {
    position: absolute; left: 104px; top: 70px; width: 928px; height: 626px;
    border-radius: 40px;
    background:
      radial-gradient(ellipse at 50% 55%, #c97aa6 0%, #d99aba 30%, rgba(238,220,237,.6) 60%, rgba(255,255,255,0) 78%),
      radial-gradient(ellipse at 20% 30%, rgba(110,150,220,.35) 0%, rgba(255,255,255,0) 45%),
      radial-gradient(ellipse at 85% 40%, rgba(120,170,90,.3) 0%, rgba(255,255,255,0) 40%);
  }

  .delivery-badge {
    position: absolute; left: 24px; top: 0; width: 324px; height: 324px;
    border-radius: 50%; background: var(--purple);
    border: 8px solid var(--white);
    color: var(--white); text-align: center;
    display: flex; flex-direction: column; align-items: center; justify-content: center;
    padding: 0 26px;
  }
  .delivery-badge .headline { font-family: "Kalam", cursive; font-weight: 700; font-size: 54px; line-height: 0.98; }
  .delivery-badge .note { font-size: 19px; line-height: 1.28; margin-top: 10px; }
  .delivery-badge .note strong { font-family: "Montserrat", sans-serif; font-weight: 700; }

  .brand-mark {
    position: absolute; left: 863px; top: 86px; width: 222px; height: 222px;
    border-radius: 50%; border: 6px solid var(--purple);
    background: var(--white);
    display: flex; align-items: center; justify-content: center; text-align: center;
    font-family: "Montserrat", sans-serif; font-weight: 600; font-size: 30px; line-height: 1.15;
    color: var(--purple);
  }

  .product-title {
    position: absolute; left: 0; right: 0; top: 640px; text-align: center;
    font-family: "Kalam", cursive; font-weight: 700; font-size: 170px; line-height: 1;
    color: var(--purple);
  }

  .price {
    position: absolute; left: 0; right: 0; top: 845px; text-align: center;
    font-family: "Montserrat", sans-serif; font-weight: 700; font-size: 46px; color: var(--purple-deep);
  }

  .description {
    position: absolute; left: 0; right: 0; top: 915px; text-align: center;
    font-size: 31px; line-height: 39px; color: var(--ink); text-transform: uppercase;
  }
  .description strong { font-family: "Montserrat", sans-serif; font-weight: 700; }

  .extras-prompt {
    position: absolute; left: 0; right: 0; top: 1078px; text-align: center;
    font-family: "Kalam", cursive; font-weight: 700; font-size: 36px; line-height: 50px; color: var(--red);
  }

  .extras {
    position: absolute; left: 230px; top: 1137px; width: 640px; height: 262px;
    display: grid; grid-template-columns: 1fr 1fr 1fr;
  }
  .extras .column { text-align: center; color: var(--ink); }
  .extras .column + .column { border-left: 2px solid var(--purple-deep); }
  .extras h3 { font-family: "Montserrat", sans-serif; font-weight: 700; font-size: 30px; line-height: 38px; }
  .extras .cost { font-family: "Montserrat", sans-serif; font-weight: 700; font-size: 30px; line-height: 40px; margin-bottom: 6px; }
  .extras li { list-style: none; font-size: 22px; line-height: 24px; }

  .claims {
    position: absolute; left: 0; right: 0; top: 1405px; text-align: center;
    font-family: "Montserrat", sans-serif; font-weight: 700; font-size: 33px; color: var(--green-dark);
  }

  .ordering {
    position: absolute; left: 30px; top: 1478px; font-size: 24px; line-height: 30px; color: var(--purple-deep);
  }
  .ordering .url { font-family: "Montserrat", sans-serif; font-weight: 700; font-size: 22px; }

  .delivery-terms {
    position: absolute; right: 30px; top: 1460px; text-align: right;
    font-size: 23px; line-height: 28px; color: var(--purple-mid);
  }
  .delivery-terms strong { font-family: "Montserrat", sans-serif; font-weight: 700; color: var(--purple-deep); }

  .footer-bar {
    position: absolute; left: 0; bottom: 0; width: 100%; height: 44px;
    display: flex; font-size: 24px; color: var(--white);
  }
  .footer-bar .contact {
    flex: 0 0 696px; background: var(--bar-dark);
    display: flex; justify-content: space-between; align-items: center; padding: 0 30px;
  }
  .footer-bar .contact strong { font-family: "Montserrat", sans-serif; font-weight: 700; }
  .footer-bar .social { display: flex; align-items: center; gap: 10px; }
  .footer-bar .social .dot { width: 20px; height: 20px; background: var(--white); border-radius: 3px; }
  .footer-bar .website {
    flex: 1; background: var(--bar-light);
    display: flex; justify-content: flex-end; align-items: center; padding: 0 30px;
    font-family: "Montserrat", sans-serif; font-weight: 600;
  }
</style>
</head>
<body>
  <main class="flyer">
    <div class="hero-photo" role="img" aria-label="Açaí bowls and a smoothie topped with strawberries, blueberries, banana slices and granola, surrounded by coconut halves, berries and a splash of water"></div>

    <div class="delivery-badge">
      <div class="headline">Now<br>delivering</div>
      <p class="note"><strong>5 bowl or smoothie</strong><br>minimum order<br><strong>No hidden delivery fees!</strong><br>Text <strong>555 730 9182</strong></p>
    </div>

    <div class="brand-mark">Peel<br>and Pulp</div>

    <h1 class="product-title">Açaí Bowl</h1>

    <p class="price">$9.00</p>

    <p class="description">
      Açaí sorbet topped with<br>
      <strong>granola, bananas, strawberries,<br>blueberries, coconut shavings</strong> and<br>
      drizzled with <strong>honey</strong>
    </p>

    <p class="extras-prompt">February only: one free topping &amp; drizzle!</p>

    <section class="extras">
      <div class="column">
        <h3>FRUITS</h3>
        <p class="cost">$1.00</p>
        <ul><li>Bananas</li><li>Blueberries</li><li>Strawberries</li></ul>
      </div>
      <div class="column">
        <h3>TOPPINGS</h3>
        <p class="cost">.50¢</p>
        <ul><li>Almonds</li><li>Cacao nibs</li><li>Chia seeds</li><li>Coconut shavings</li><li>Granola</li><li>Hemp seeds</li><li>Quinoa puffs</li></ul>
      </div>
      <div class="column">
        <h3>DRIZZLE</h3>
        <p class="cost">.50¢</p>
        <ul><li>Agave</li><li>Almond butter</li><li>Honey</li><li>Peanut butter</li></ul>
      </div>
    </section>

    <p class="claims">100% AÇAÍ - ORGANIC - VEGAN</p>

    <div class="ordering">
      <p>Online ordering through website:</p>
      <p class="url">https://tillbox.example/shop/peelandpulp</p>
    </div>

    <div class="delivery-terms">
      <p><strong>FRIDAY DELIVERIES ONLY</strong></p>
      <p>All orders must be placed</p>
      <p><strong>by 5:00 pm</strong> the day before delivery</p>
    </div>

    <footer class="footer-bar">
      <div class="contact">
        <span>Questions? <strong>Call (555) 730-9182</strong></span>
        <span class="social"><span class="dot"></span>@pnpulp</span>
      </div>
      <div class="website">www.peelandpulp.example</div>
    </footer>
  </main>
</body>
</html>
```